Engineering Consultant Business Card

I'm starting a new business as a high-end engineering consultant in a niche field. I've attached the jpg for my logo plus the branding guideline document that I've been following. You can see my business website here: www.tarvikworks.com
I'd like a business card that has the logo on one side, then the other side has (in any order): Tarvik Works, Inc.
Dana Whitlock
President and Chief EMC Engineer
www.tarvikworks.com
dana@tarvikworks.com
Optional: motto "We will solve your EMC problems as early as possible—ideally before they even start."
I'm not planning on including a phone number
Target Market(s)
Businesses, especially makers of electronics hardware
Industry/Entity Type
Electrical engineering
Contact Information for Business Card
Company name, my name, website, email

```html
<!DOCTYPE html>
<html lang="en">
<head>
<meta charset="utf-8">
<title>Tarvik Works – Business Card</title>
<link rel="stylesheet" href="https://fonts.googleapis.com/css2?family=Lexend:wght@300;400;600&display=swap">
<style>
  :root {
    --backdrop: #e6e6e6;
    --card-blue: #2f4592;
    --pattern-blue: #3a58c4;
    --ink: #ffffff;
  }
  html, body {
    margin: 0;
    padding: 0;
    width: 1200px;
    height: 1052px;
    overflow: hidden;
    background: var(--backdrop);
    font-family: "Lexend", sans-serif;
  }
  .canvas { position: relative; width: 1200px; height: 1052px; }
  .card {
    position: absolute;
    top: 112px;
    width: 479px;
    height: 838px;
    border-radius: 36px;
    background: var(--card-blue);
    box-shadow: 0 6px 22px rgba(0,0,0,0.22);
    overflow: hidden;
    color: var(--ink);
  }
  .card--front { left: 80px; }
  .card--back { left: 608px; }

  .brand {
    position: absolute;
    left: 0; right: 0;
    display: flex;
    align-items: center;
    justify-content: center;
    gap: 12px;
    font-weight: 600;
    color: var(--ink);
    white-space: nowrap;
  }
  .brand__dot {
    border-radius: 50%;
    border: 4px solid var(--ink);
    box-sizing: border-box;
  }
  .card--front .brand { top: 192px; font-size: 40px; }
  .card--front .brand__dot { width: 46px; height: 46px; }

  .holder-name {
    position: absolute; top: 382px; left: 0; right: 0;
    text-align: center; font-size: 38px; font-weight: 600; margin: 0;
  }
  .holder-title {
    position: absolute; top: 434px; left: 0; right: 0;
    text-align: center; font-size: 21px; font-weight: 300; margin: 0;
  }
  .contact-rule {
    position: absolute; top: 522px; left: 80px; width: 318px; height: 32px;
  }
  .contact-list {
    position: absolute; top: 572px; left: 0; right: 0;
    text-align: center; font-size: 21px; font-weight: 300; line-height: 29px;
    margin: 0;
  }
  .divider {
    position: absolute; top: 648px; left: 64px; width: 351px;
    height: 0; border-top: 1.5px solid var(--ink);
  }
  .motto {
    position: absolute; top: 661px; left: 0; right: 0;
    text-align: center; font-size: 22px; font-weight: 300; line-height: 28px;
    margin: 0;
  }

  .back-pattern {
    position: absolute; inset: 0;
    background:
      linear-gradient(180deg, rgba(58,88,196,0.55) 0%, rgba(58,88,196,0.45) 70%, rgba(47,69,146,0) 100%),
      var(--card-blue);
  }
  .card--back .brand { top: 585px; font-size: 27px; }
  .card--back .brand__dot { width: 32px; height: 32px; border-width: 3px; }
</style>
</head>
<body>
<main class="canvas">
  <section class="card card--front" aria-label="Business card front">
    <div class="brand"><span class="brand__dot"></span><span>Tarvik Works</span></div>
    <h1 class="holder-name">Dana Whitlock</h1>
    <p class="holder-title">President and Chief EMC Engineer</p>
    <svg class="contact-rule" viewBox="0 0 318 32" aria-hidden="true">
      <line x1="0" y1="16" x2="112" y2="16" stroke="#fff" stroke-width="1.5"/>
      <line x1="206" y1="17" x2="318" y2="17" stroke="#fff" stroke-width="1.5"/>
      <rect x="122" y="0" width="32" height="34" rx="4" fill="#fff"/>
      <rect x="128" y="9" width="20" height="15" fill="none" stroke="#2f4592" stroke-width="1.8"/>
      <polyline points="128,9 138,18 148,9" fill="none" stroke="#2f4592" stroke-width="1.8"/>
      <line x1="128" y1="24" x2="135" y2="17" stroke="#2f4592" stroke-width="1.4"/>
      <line x1="148" y1="24" x2="141" y2="17" stroke="#2f4592" stroke-width="1.4"/>
      <rect x="164" y="1" width="32" height="33" rx="4" fill="#fff"/>
      <circle cx="180" cy="17" r="9" fill="none" stroke="#2f4592" stroke-width="1.8"/>
      <ellipse cx="180" cy="17" rx="4" ry="9" fill="none" stroke="#2f4592" stroke-width="1.5"/>
      <line x1="171" y1="17" x2="189" y2="17" stroke="#2f4592" stroke-width="1.5"/>
      <line x1="172.5" y1="12.5" x2="187.5" y2="12.5" stroke="#2f4592" stroke-width="1.2"/>
      <line x1="172.5" y1="21.5" x2="187.5" y2="21.5" stroke="#2f4592" stroke-width="1.2"/>
    </svg>
    <p class="contact-list">
      <span class="contact-email">dana@tarvikworks.com</span><br>
      <span class="contact-web">www.tarvikworks.com</span>
    </p>
    <div class="divider"></div>
    <p class="motto">We will solve your EMC problems<br>as early as possible ideally<br>before they even start.</p>
  </section>

  <section class="card card--back" aria-label="Business card back">
    <div class="back-pattern" role="img" aria-label="Faint repeating brand pattern fading toward the bottom"></div>
    <div class="brand"><span class="brand__dot"></span><span>Tarvik Works</span></div>
  </section>
</main>
</body>
</html>
```